A website for a green bio-plastics manufacturing company

We need a home page designed and two complimentary template pages that can be used for the rest of the website. The template page should vary in design from the home page, but should flow uniformly with it.

This is a very innovative company with a proprietary manufacturing method of using bird feathers to make plastic.

The site should be functional, informative, user-friendly and informative to both our business partners and the consumers.
Updates

I've added a more concise overview of the company.  If any of the designers have any questions for me, please ask.  Thanks

Marco

Target Market(s)

Business partners interested in using bio-plastics for their products and general customers.

Industry/Entity Type

Manufacturing

Number of Pages Required

3 pages

Requirements
Must have
• I attached some information about the company, so the site should be designed to incorporate that content.

Will need to be edited by Adobe Contribute.

Easy to navigate

One of the template pages should have one column for content. The other should have two columns. I''m open to different ideas though.

Should be very pleasing to the eye and uncluttered.

Want to be informative to both our business partners as well as consumers who may be researching our product(s)

Easy to Maintain

Anticipated Tabs/Pages
· Home Page
o General “welcome” page

· About Us
o Company overview and information

· Products
o Horticulture Containers
o Agriculture Films
o Where to Buy
o Upcoming Products

· Business Partners

· Press Releases

· Contact Us

Nice to have
• Would like to have earth tones and or nice greens in the color scheme. They make use of bird feathers for their manufacturing process, so perhaps a real sharp image of a feather can be incorporated into the design. Be creative though.

Perhaps a jQuery nav bar, but that may be out of scope.

Should not have
• No flash at all.

```html
<!DOCTYPE html>
<html lang="en">
<head>
<meta charset="utf-8">
<title>Verdant Polymer Works</title>
<link rel="stylesheet" href="https://fonts.googleapis.com/css2?family=Open+Sans:ital,wght@0,400;0,600;0,700;1,700&family=Roboto:wght@300;400&display=swap">
<style>
:root{
  --leaf:#7fa80c;
  --leaf-light:#a9cc2a;
  --leaf-dark:#5d8a05;
  --ink:#111;
  --body:#333;
  --muted:#888;
  --accent:#e05a10;
  --orange-top:#ffb52a;
  --orange-bottom:#ff8a00;
  --rule:#dcdcdc;
  --panel:#f1f1ec;
  --footer:#eff0ea;
  --white:#fff;
}
*{box-sizing:border-box;margin:0;padding:0}
html,body{width:1023px;height:1200px;overflow:hidden;background:var(--white)}
body{position:relative;font-family:"Open Sans",Arial,sans-serif;color:var(--body)}
a{color:inherit;text-decoration:none}

.brand{position:absolute;left:34px;top:34px;display:flex;align-items:center;gap:12px}
.brand-dot{width:64px;height:64px;border-radius:50%;background:var(--leaf)}
.brand-name{font-family:"Open Sans",sans-serif;font-weight:600;font-size:27px;line-height:30px;color:#2a2a2a;letter-spacing:.5px}

.main-nav{position:absolute;top:70px;left:400px;right:16px;display:flex;justify-content:space-between}
.main-nav a{font-family:Arial,"Open Sans",sans-serif;font-size:14px;color:var(--ink)}
.main-nav a::after{content:"\2192";color:var(--accent);font-size:12px;margin-left:3px;font-weight:700}

.hero{position:absolute;left:32px;top:119px;width:958px;height:309px;
  background:linear-gradient(90deg,#8ab812 0%,#9cc41e 35%,#86b00c 100%);
  border-bottom:3px solid #c8d9a0}
.hero-art{position:absolute;left:40px;top:0;width:470px;height:300px;
  background:radial-gradient(circle at 45% 45%,#d6e84a 0%,#8cb818 45%,rgba(140,184,24,0) 70%)}
.hero-title{position:absolute;left:485px;top:48px;font-family:Roboto,sans-serif;font-weight:300;font-size:42px;color:var(--white);letter-spacing:-1px}
.hero-text{position:absolute;left:488px;top:126px;width:440px;font-family:Roboto,sans-serif;font-weight:300;font-size:21px;line-height:25px;color:var(--white)}
.hero-button{position:absolute;left:576px;top:219px;width:330px;height:43px;border-radius:3px;
  background:linear-gradient(var(--orange-top),var(--orange-bottom));border:1px solid #f07000;
  font-family:Arial,sans-serif;font-size:16px;color:#c0260a;display:flex;align-items:center;justify-content:center}

.featured{position:absolute;left:32px;top:480px;width:248px;height:503px;background:var(--panel);
  border:1px solid #d4d4d0;border-radius:3px;z-index:2}
.featured-head,.news-head{height:39px;display:flex;align-items:center;padding-left:26px;font-size:18px}
.featured-head{background:linear-gradient(#a4c62e,#7aa20a);color:var(--white)}
.product-card{position:absolute;left:8px;width:229px;background:var(--white);border-radius:4px;padding:0 20px}
.product-card.first{top:59px;height:213px}
.product-card.second{top:283px;height:212px}
.product-photo{height:110px;width:130px;margin-top:10px;border-radius:50%}
.first .product-photo{background:radial-gradient(ellipse,#b6d77a 0%,#dbebc0 55%,#fff 72%)}
.second .product-photo{background:radial-gradient(ellipse,#9cc8ec 0%,#d4e8f6 55%,#fff 72%)}
.product-title{margin-top:6px;font-family:Verdana,sans-serif;font-weight:700;font-size:10.5px;letter-spacing:.5px;color:var(--accent);text-decoration:underline}
.product-text{font-family:Verdana,sans-serif;font-size:10.5px;line-height:15px;color:#222}
.more{display:block;margin-top:14px;width:11px;height:11px;border-radius:50%;background:var(--accent);position:relative}
.more::after{content:"";position:absolute;left:4px;top:3px;border-left:4px solid #fff;border-top:2.5px solid transparent;border-bottom:2.5px solid transparent}

.stories{position:absolute;left:328px;top:486px;width:381px;z-index:2}
.story{position:relative;height:196px;border-bottom:1px solid var(--rule)}
.story:last-child{border-bottom:none;height:170px}
.story + .story{padding-top:26px}
.story-title{font-size:22px;line-height:23px;letter-spacing:-.8px;color:#000;font-weight:400}
.story-title .go{display:inline-block;width:17px;height:17px;border-radius:50%;background:var(--accent);vertical-align:-2px;position:relative}
.story-title .go::after{content:"\2192";position:absolute;left:3px;top:-4px;color:#fff;font-size:12px;font-weight:700}
.story-body{margin-top:14px;display:flex;justify-content:space-between;gap:10px}
.story-body.icon-left{flex-direction:row-reverse}
.story-copy{width:300px;font-family:Verdana,sans-serif;font-size:10.5px;line-height:15px;color:#222}
.story-copy em{display:block;font-weight:700;font-size:10.5px}
.story-icon{flex:none;width:70px;height:68px;border-radius:6px;background:linear-gradient(135deg,#bdbdbd,#4a4a4a)}

.news{position:absolute;left:759px;top:480px;width:231px;height:335px;border:1px solid #d4d4d0;border-radius:3px;z-index:2;background:var(--white)}
.news-head{background:linear-gradient(#fff,#e4e4e4);color:var(--ink);padding-left:16px}
.news-item{padding:26px 16px 0 17px;font-family:Verdana,sans-serif;font-size:10.5px;line-height:15px}
.news-item h3{font-size:10.5px;font-weight:700;color:var(--ink)}
.news-date{color:var(--muted);margin-bottom:8px}
.news-item a{color:var(--accent);text-decoration:underline}

.badge{position:absolute;left:796px;top:847px;width:168px;height:168px;border-radius:50%;z-index:2;
  background:radial-gradient(circle at 40% 35%,#a6cc2a,#6c9a06);box-shadow:0 4px 8px rgba(0,0,0,.2);
  color:var(--white);font-family:Arial,sans-serif;font-weight:700;padding:34px 0 0 20px}
.badge-big{font-size:42px;line-height:40px;letter-spacing:-2px}
.badge-small{font-size:17px;line-height:18px;padding-left:16px}
.badge-link{font-size:17px;color:#1e3000;text-decoration:underline;padding-left:26px}

.feather-band{position:absolute;left:32px;top:1014px;width:958px;height:66px;z-index:0;
  background:linear-gradient(rgba(255,255,255,0),#e6eedb)}
.footer{position:absolute;left:32px;top:1080px;width:958px;height:107px;background:var(--footer);
  border-top:3px solid #c8d4b8;font-size:12.5px;color:#222}
.footer-nav{position:absolute;left:30px;top:24px}
.footer-nav span{margin:0 6px}
.footer-legal{position:absolute;right:15px;top:26px;font-family:Verdana,sans-serif;font-size:11px}
.footer-legal a{text-decoration:underline}
</style>
</head>
<body>

<header>
  <a class="brand" href="#"><span class="brand-dot"></span><span class="brand-name">Verdant<br>Polymer Works</span></a>
  <nav class="main-nav">
    <a href="#">About Us</a><a href="#">Products</a><a href="#">Business Partners</a><a href="#">Press Releases</a><a href="#">Contacts</a>
  </nav>
</header>

<section class="hero">
  <div class="hero-art" role="img" aria-label="Green globe resting in grass beside a feather"></div>
  <h1 class="hero-title">Welcome to Our Site!</h1>
  <p class="hero-text">Sed ut perspiciatis unde omnis iste natus error sit voluptatem accustium doremque launtium.</p>
  <a class="hero-button" href="#">CLICK HERE TO LEARN MORE</a>
</section>

<div class="feather-band" role="img" aria-label="Row of soft white feathers"></div>

<aside class="featured">
  <h2 class="featured-head">Featured Products</h2>
  <div class="product-card first">
    <div class="product-photo" role="img" aria-label="Green biodegradable plant tray"></div>
    <a class="product-title" href="#">LOREM IPSUM DOLOR SIT</a>
    <p class="product-text">Consectetur adipisicing elit, sed iusmod tempor incididunt utabore olore magna aliqua.</p>
    <a class="more" href="#" aria-label="More"></a>
  </div>
  <div class="product-card second">
    <div class="product-photo" role="img" aria-label="Clear blue bioplastic containers"></div>
    <a class="product-title" href="#">IPSUM DOLOR SIT</a>
    <p class="product-text">Consectetur adipisicing elit, sed iusmod tempor incid utaboreolore magna aliqua.</p>
    <a class="more" href="#" aria-label="More"></a>
  </div>
</aside>

<main class="stories">
  <article class="story">
    <h2 class="story-title">Sed ut perspiciatis unde omnis&nbsp; natus error sitvolup <span class="go"></span></h2>
    <div class="story-body">
      <p class="story-copy"><em>Sed ut perspiciatis unde omnis iste natus</em>Error itatem accusantium doloremque laudanti ttam aperiam, eue ipsa quae ab illo inventore verittieasi archecto beatatae dicta sunt explicabo. Nemoipsam oluptatem quia voluptas.</p>
      <div class="story-icon" role="img" aria-label="Floppy disk and CD icon"></div>
    </div>
  </article>
  <article class="story">
    <h2 class="story-title">Perspiciatis unde omniste natus error sitvolup <span class="go"></span></h2>
    <div class="story-body icon-left">
      <p class="story-copy"><em>Perspiciatis unde omnis iste natus</em>Error itatem accusantium doloremque laudanti totam aperiam, eue ipsa quae ab illo inventore veritis easi archecto beatatae dicta sunt explicabo. Nemo ipsam oluptatem quia voluptas sit aspernatur.</p>
      <div class="story-icon" role="img" aria-label="Address book icon"></div>
    </div>
  </article>
  <article class="story">
    <h2 class="story-title">Omiste natus error sitatem cusantium doloremque laudantium <span class="go"></span></h2>
    <div class="story-body">
      <p class="story-copy"><em>Error itatem accusantium</em>Doloremque laudantium, totam aperiam, e ipsa quae ab illo inventore veritatis easi archecto beatatae dicta sunt explicabo. Nemo ipsam oluptatem quia voluptas sit aspernatur.</p>
      <div class="story-icon" role="img" aria-label="Folder with keys icon"></div>
    </div>
  </article>
</main>

<aside class="news">
  <h2 class="news-head">News &amp; Events</h2>
  <div class="news-item">
    <h3>Unde omnis iste natus error itatem</h3>
    <p class="news-date">Posted: 12/07/2008</p>
    <p>Doloremque laudantium, tperiam, eue ipsa quae <a href="#">ab illontore veritatis</a> easi archecto beatatae.</p>
  </div>
  <div class="news-item">
    <h3>Doloremque laudantiu tperiam</h3>
    <p class="news-date">Posted: 12/07/2008</p>
    <p>Daudantium, tperiam, eue ipsquae ab illontore veritatis easi archecto beatatadicta <a href="#">sunt explicabo</a>. Nemo ipsam oluptatem quia</p>
  </div>
</aside>

<a class="badge" href="#">
  <div class="badge-big">100%</div>
  <div class="badge-small">renewable<br>biomass</div>
  <div class="badge-link">click here</div>
</a>

<footer class="footer">
  <nav class="footer-nav">
    <a href="#">Company</a><span>|</span><a href="#">Products</a><span>|</span><a href="#">Business Partners</a><span>&nbsp;|</span><a href="#">Support</a><span>|</span><a href="#">Contacts</a>
  </nav>
  <p class="footer-legal">VERDANT POLYMER WORKS &nbsp; 2010 | <a href="#">Privacy Policy</a></p>
</footer>

</body>
</html>
```